Coaching company requires a Bi-Fold Services Brochure

**Please also read attached design brief***

As part of our expanding sales role for our Professional Development Company, we need a Bi-Fold services brochure that offers our clients some further information about our specific services.

This services brochure will be the document that our clients will receive after our initial contact with them so the overall design of this document will play an instrumental part in our securing of ongoing work.

We have prepared a design brief for designers that want to undertake this task and this document should help to clarify any missing information from this online brief. Any designer who is interested in submitting a design should also refer to this attached document to get the full scope of the works required.

Regular email correspondence will also be available to clarify any questions that the design may have

*** Please also note that the finished design will need to be submitted in a PSD format to allow for editing in Photoshop CS6

Target Market(s)

Our target market is Business to Business. We are specifically targeting small, medium and large businesses who are looking to invest in Professional Development for their business and their staff.
The areas of major focus are 1 on 1 coaching of leaders, executives & business owners and group facilitation sessions with their staff.

Industry/Entity Type

Business Service

Font styles to use
Sans Serif

Requirements
Must have
• - Design needs to be an A4 Bi-Fold layout so should suit an A3 sheet of paper (297mm x 420mm)
• - Include our corporate color scheme
• - Finished design must be in PSD format or format that can be edited in Photshop CS6
• - Appealing to small, medium and large businesses (universal appeal)
• - The project must be in CMYK Colour and no less than 300 pixel resolution
Nice to have
• - Our logo incorporated into the front page
• - We would like the images used in this brochure to be happy and vibrant (i.e. smiling faces and energetic etc.)

```html
<!DOCTYPE html>
<html lang="en">
<head>
<meta charset="utf-8">
<title>Northway Learning – Services Brochure</title>
<link href="https://fonts.googleapis.com/css2?family=Open+Sans:wght@400;600;700&family=Raleway:wght@300;400;600;700&display=swap" rel="stylesheet">
<style>
  :root {
    --blue: #2a9fd8;
    --blue-dark: #1b7fb4;
    --blue-light: #8fd0f0;
    --ink: #4a4f55;
    --muted: #7d848b;
    --paper: #ffffff;
    --stage: #e9ecef;
  }
  * { box-sizing: border-box; margin: 0; padding: 0; }
  html, body { width: 863px; height: 1200px; overflow: hidden; }
  body {
    background: var(--stage);
    font-family: "Open Sans", Arial, sans-serif;
    color: var(--ink);
    padding: 12px 20px;
    display: flex; flex-direction: column; gap: 12px;
  }
  .spread {
    width: 823px; height: 582px;
    display: grid; grid-template-columns: 1fr 1fr;
    background: var(--paper);
    box-shadow: 0 2px 8px rgba(0,0,0,.18);
    overflow: hidden;
  }
  .page { position: relative; overflow: hidden; }
  .photo { display: block; }
  p { font-size: 6.4px; line-height: 1.55; }

  /* Brand name: plain text, one colour, one weight */
  .brand { font-family: "Raleway", sans-serif; font-weight: 400; color: var(--ink); letter-spacing: 0; }

  /* ---------- Back cover ---------- */
  .back-top { position: absolute; left: 0; top: 0; width: 100%; height: 270px; background: var(--blue); }
  .back-intro { position: absolute; left: 22px; top: 24px; width: 200px; color: #fff; }
  .back-intro p { color: #eaf6fd; margin-bottom: 6px; }
  .back-intro .lead { font-family: "Raleway", sans-serif; font-size: 11px; font-weight: 600; margin-bottom: 8px; line-height: 1.3; color: #fff; }
  .back-coach { position: absolute; right: 0; top: 0; width: 178px; height: 248px;
    background: linear-gradient(160deg,#f3f6f8,#c9d3db 60%,#7f8e99); }
  .back-phone { position: absolute; left: 22px; top: 218px; color: #fff; display: flex; align-items: center; gap: 6px;
    font-family: "Raleway", sans-serif; font-weight: 700; font-size: 15px; }
  .back-curve { position: absolute; left: 0; top: 240px; width: 100%; height: 50px; }
  .back-brand { position: absolute; left: 0; width: 100%; top: 330px; text-align: center; font-size: 26px; }
  .back-strip { position: absolute; left: 22px; right: 22px; top: 392px; height: 62px; display: grid; grid-template-columns: repeat(4,1fr); gap: 4px; }
  .back-strip .photo:nth-child(1){ background: linear-gradient(135deg,#c9a98c,#6f7c88); }
  .back-strip .photo:nth-child(2){ background: linear-gradient(135deg,#b9c6d1,#59697a); }
  .back-strip .photo:nth-child(3){ background: linear-gradient(135deg,#d6c3b0,#7f8a94); }
  .back-strip .photo:nth-child(4){ background: linear-gradient(135deg,#a7b7c4,#4e5d6b); }
  .back-band { position: absolute; left: 0; right: 0; top: 470px; height: 34px; background: var(--blue-light);
    display: flex; align-items: center; padding-left: 22px; color: #fff;
    font-family: "Raleway", sans-serif; font-size: 12px; font-weight: 600; }
  .back-band em { font-style: normal; font-size: 8px; font-weight: 400; margin-left: 6px; }

  /* ---------- Front cover ---------- */
  .front-head { position: absolute; left: 0; top: 0; right: 0; height: 92px; display: flex; justify-content: center; align-items: center; font-size: 24px; }
  .front-web { position: absolute; right: 26px; top: 100px; font-size: 7px; color: var(--muted); }
  .front-photo { position: absolute; left: 0; right: 0; top: 118px; height: 255px;
    background: linear-gradient(180deg,#f4f7f9 0%,#d8dde2 35%,#8a98a6 75%,#3f4c59 100%); }
  .front-swoosh { position: absolute; left: 0; top: 330px; width: 100%; height: 80px; }
  .front-title { position: absolute; left: 0; right: 0; top: 420px; text-align: center; }
  .front-title h1 { font-family: "Raleway", sans-serif; font-weight: 300; color: var(--blue); font-size: 28px; letter-spacing: 2px; }
  .front-title p { font-family: "Raleway", sans-serif; font-size: 9px; color: var(--ink); margin-top: 4px; }
  .front-title p em { font-style: normal; color: var(--muted); font-size: 7px; }
  .front-base { position: absolute; left: 0; right: 0; bottom: 0; height: 18px; background: var(--blue-light); }

  /* ---------- Inside left ---------- */
  .inside-left { padding: 18px 20px; }
  .section-title { font-family: "Raleway", sans-serif; font-weight: 600; color: var(--blue); font-size: 14px; margin-bottom: 6px; }
  .about { display: grid; grid-template-columns: 1fr 1fr; gap: 12px; }
  .about h4 { font-size: 6.8px; color: var(--blue); font-weight: 700; margin: 5px 0 2px; }
  .about p + p { margin-top: 4px; }
  .deliver { display: grid; grid-template-columns: 1fr 1fr; gap: 12px; margin-top: 8px; }
  .deliver h4 { font-size: 8px; color: var(--blue); font-weight: 700; margin-bottom: 3px; }
  .deliver-photo { height: 96px; background: linear-gradient(135deg,#dfe6eb,#7c8c99); }
  .testimonials { position: absolute; left: 0; right: 0; bottom: 0; height: 250px; background: var(--blue); color: #fff; padding: 20px 20px 14px; }
  .testimonials .section-title { color: #fff; font-size: 15px; }
  .testimonials .cols { display: grid; grid-template-columns: 1fr 1fr; gap: 14px; }
  .testimonials p { color: #eaf6fd; margin-bottom: 5px; }
  .testimonials .who { font-weight: 700; color: #fff; font-style: italic; margin-bottom: 9px; }
  .testi-curve { position: absolute; left: 0; top: -28px; width: 100%; height: 30px; }

  /* ---------- Inside right ---------- */
  .services-band { height: 30px; background: var(--blue); color: #fff; display: flex; align-items: center; padding-left: 20px;
    font-family: "Raleway", sans-serif; font-weight: 700; font-size: 17px; letter-spacing: 1px; margin-top: 16px; }
  .services { display: grid; grid-template-columns: 1fr 1fr; gap: 14px; padding: 10px 20px; }
  .services h3 { font-family: "Raleway", sans-serif; color: var(--blue); font-size: 10px; font-weight: 700; letter-spacing: .5px; margin: 6px 0 4px; }
  .services h4 { font-size: 7px; color: var(--ink); font-weight: 700; margin: 6px 0 2px; }
  .services p { margin-bottom: 4px; }
  .services-photo { height: 100px; margin-top: 6px; background: linear-gradient(135deg,#e4d6c6,#8596a4); }
</style>
</head>
<body>

<section class="spread">
  <article class="page back">
    <div class="back-top"></div>
    <div class="back-intro">
      <p class="lead">Helping your people grow, lead and perform at their very best.</p>
      <p>We partner with businesses of every size to build confident leaders and focused teams. Our coaching and facilitation programs are practical, tailored and measured against real outcomes.</p>
      <p>From one-on-one sessions with owners and executives to group workshops with staff, we bring structure, energy and clear goals to every engagement.</p>
      <p>Talk with us about where your business is heading and how your people can take it there.</p>
    </div>
    <div class="photo back-coach" role="img" aria-label="Photo of a coach presenting at a whiteboard"></div>
    <svg class="back-curve" viewBox="0 0 411 50" preserveAspectRatio="none" aria-hidden="true">
      <path d="M0 36 Q205 0 411 26 L411 50 L0 50 Z" fill="#fff"/>
    </svg>
    <div class="back-phone">
      <svg width="14" height="14" viewBox="0 0 24 24" aria-hidden="true"><path fill="#fff" d="M6.6 10.8a15 15 0 006.6 6.6l2.2-2.2a1 1 0 011-.25 11.4 11.4 0 003.6.57 1 1 0 011 1V20a1 1 0 01-1 1A17 17 0 013 4a1 1 0 011-1h3.5a1 1 0 011 1c0 1.25.2 2.45.57 3.57a1 1 0 01-.25 1z"/></svg>
      1300 555 014
    </div>
    <div class="back-brand brand">Northway Learning</div>
    <div class="back-strip">
      <div class="photo" role="img" aria-label="Photo of a smiling businesswoman"></div>
      <div class="photo" role="img" aria-label="Photo of a team meeting"></div>
      <div class="photo" role="img" aria-label="Photo of colleagues collaborating"></div>
      <div class="photo" role="img" aria-label="Photo of a group workshop"></div>
    </div>
    <div class="back-band">Professional Development Company <em>– for all kinds of business</em></div>
  </article>

  <article class="page front">
    <header class="front-head brand">Northway Learning</header>
    <div class="front-web">www.northwaylearning.example</div>
    <div class="photo front-photo" role="img" aria-label="Photo of a cheerful business team giving thumbs up"></div>
    <svg class="front-swoosh" viewBox="0 0 411 80" preserveAspectRatio="none" aria-hidden="true">
      <path d="M0 50 Q200 10 411 40 L411 80 L0 80 Z" fill="#fff"/>
      <path d="M0 46 Q200 4 411 34" fill="none" stroke="#2a9fd8" stroke-width="4"/>
      <path d="M0 56 Q220 18 411 48" fill="none" stroke="#8fd0f0" stroke-width="2"/>
    </svg>
    <div class="front-title">
      <h1>SERVICES BROCHURE</h1>
      <p>Professional Development Company <em>– for all kinds of business</em></p>
    </div>
    <div class="front-base"></div>
  </article>
</section>

<section class="spread">
  <article class="page inside-left">
    <h2 class="section-title">About us</h2>
    <div class="about">
      <div>
        <p>We are a professional development company that works with leaders, owners and teams to lift performance. Our programs combine proven methods with honest, practical conversation.</p>
        <h4>Our Purpose</h4>
        <p>To help people and businesses reach their potential through clear goals and lasting habits.</p>
        <h4>Our Vision</h4>
        <p>Workplaces where every person feels capable, valued and ready to lead.</p>
      </div>
      <div>
        <p>Every engagement begins by listening. We learn how your business works, where it wants to go and what stands in the way, then design sessions around that picture.</p>
        <p>Our facilitators bring years of experience across many industries and business sizes, so advice is grounded and relevant.</p>
      </div>
    </div>
    <div class="deliver">
      <div>
        <h4>How we deliver results</h4>
        <p>We set measurable goals at the start, check progress at each step and adjust as your people grow. Clients receive clear summaries and follow-up support after every program.</p>
      </div>
      <div class="photo deliver-photo" role="img" aria-label="Photo of a mentor speaking with a colleague"></div>
    </div>
    <div class="testimonials">
      <svg class="testi-curve" viewBox="0 0 411 30" preserveAspectRatio="none" aria-hidden="true">
        <path d="M0 30 Q200 0 411 22 L411 30 Z" fill="#2a9fd8"/>
      </svg>
      <h2 class="section-title">Testimonials</h2>
      <div class="cols">
        <div>
          <p>"The coaching sessions gave our managers real confidence. We noticed better meetings and clearer decisions within weeks."</p>
          <p class="who">– Operations Manager, Logistics Firm</p>
          <p>"Practical, friendly and focused. Our team left the workshop with a plan we actually use every day."</p>
          <p class="who">– Director, Retail Group</p>
        </div>
        <div>
          <p>"As a small business owner I needed someone to challenge my thinking. The one-on-one program did exactly that."</p>
          <p class="who">– Owner, Design Studio</p>
          <p>"Well structured sessions and genuine follow-up. We have booked a second round for our new leaders."</p>
          <p class="who">– HR Lead, Finance Company</p>
        </div>
      </div>
    </div>
  </article>

  <article class="page inside-right">
    <div class="services-band">OUR SERVICES</div>
    <div class="services">
      <div>
        <h3>COACHING</h3>
        <h4>Regular Client / Leadership Coaching</h4>
        <p>Ongoing one-on-one sessions for leaders, executives and owners. We work on goals, communication and decision making at a steady, sustainable pace.</p>
        <h4>Executive Coaching</h4>
        <p>Focused support for senior people facing change, growth or new responsibility. Sessions are confidential, direct and built around your priorities.</p>
        <h4>Small Business Coaching</h4>
        <p>Guidance for owners balancing many roles. We help set priorities, build systems and free up time to work on the business.</p>
        <div class="photo services-photo" role="img" aria-label="Photo of a coaching session between two professionals"></div>
      </div>
      <div>
        <h3>GROUP FACILITATION</h3>
        <p>Interactive workshops for teams of any size. Sessions cover leadership, teamwork, communication and planning, with activities that keep people engaged.</p>
        <p>We facilitate strategy days, team reviews and staff development programs, on site or at a venue of your choice.</p>
        <p>Each session ends with clear actions and a short report so the momentum continues back at work.</p>
        <h3>CUSTOMISED COURSES</h3>
        <p>Need something specific? We design courses around your goals, culture and people, from single sessions to full programs.</p>
        <p>Talk with us about timing, group size and outcomes, and we will build a proposal that fits your business.</p>
      </div>
    </div>
  </article>
</section>

</body>
</html>
```